Business Card Design using new logo

As much as we'd like to think that treating everyone equally is the best strategy for fairness, the reality is that the differences in the lives of women and men have to be taken into account to ensure that organizations, programs, services, and yes, even public policy treat women and men in ways that achieve gender equity.

That's where ParityLumen - fairness metrics insight comes in. Using the data-driven tools of gender analysis, our organization can help anyone determine if gender equity is being achieved - in businesses and organizations, in the planning and implementation of programs and services, and in the development and enforcement of public policy.
Updates

Apologies for the delay - have not had time to finalize the decision.  Should be early this week - probably Tuesday.

Industry/Entity Type

Business

Requirements
Must have
• New Logo for ParityLumen
• Logo plus words "Fairness Metrics Insight"

```html
<!DOCTYPE html>
<html lang="en">
<head>
<meta charset="utf-8">
<title>ParityLumen – Business Card</title>
<link rel="stylesheet" href="https://fonts.googleapis.com/css2?family=Open+Sans:wght@400;600;700&display=swap">
<style>
  :root {
    --orange: #f39a1e;
    --orange-deep: #e8860f;
    --ink: #2b2b2b;
    --grey: #5a5a5a;
    --paper: #ffffff;
    --backdrop: #ecebe8;
  }
  * { box-sizing: border-box; margin: 0; padding: 0; }
  html, body { width: 1200px; height: 1024px; overflow: hidden; }
  body {
    background: var(--backdrop);
    font-family: "Open Sans", Arial, sans-serif;
    position: relative;
  }
  .card {
    position: absolute;
    left: 200px;
    width: 800px;
    height: 457px;
    border-radius: 4px;
    box-shadow: 0 6px 18px rgba(0,0,0,0.15);
    overflow: hidden;
  }
  .card--front { top: 40px; background: var(--paper); }
  .card--back {
    top: 527px;
    background: linear-gradient(135deg, var(--orange) 0%, var(--orange-deep) 100%);
  }

  .brand { display: flex; align-items: center; gap: 18px; }
  .brand__dot { border-radius: 50%; flex: none; }
  .brand__text { display: flex; flex-direction: column; }
  .brand__name { font-weight: 600; letter-spacing: -0.5px; line-height: 1; }
  .brand__tagline { font-weight: 400; text-transform: uppercase; letter-spacing: 2.5px; line-height: 1; margin-top: 10px; }

  .card--front .brand { position: absolute; left: 70px; top: 62px; }
  .card--front .brand__dot { width: 62px; height: 62px; background: var(--orange); }
  .card--front .brand__name { font-size: 64px; color: var(--ink); }
  .card--front .brand__tagline { font-size: 15px; color: var(--grey); }

  .holder { position: absolute; left: 70px; top: 200px; }
  .holder__line { font-size: 24px; font-weight: 700; color: var(--orange); text-transform: uppercase; letter-spacing: 0.5px; }
  .holder__title { color: var(--grey); font-weight: 400; font-size: 19px; }
  .holder__address { margin-top: 12px; font-size: 18px; color: var(--grey); line-height: 1.45; }

  .contacts { position: absolute; left: 70px; top: 338px; font-size: 17px; color: var(--grey); }
  .contacts__row { display: flex; align-items: center; gap: 20px; margin-bottom: 10px; }
  .contact { display: flex; align-items: center; gap: 7px; }
  .contact svg { width: 16px; height: 16px; flex: none; }
  .contact__square { width: 14px; height: 14px; background: var(--orange); border-radius: 2px; flex: none; }

  .card--back .brand { position: absolute; left: 50%; top: 50%; transform: translate(-50%, -60%); }
  .card--back .brand__dot { width: 66px; height: 66px; background: var(--paper); }
  .card--back .brand__name { font-size: 70px; color: var(--paper); }
  .card--back .brand__tagline { font-size: 16px; color: var(--paper); }
  .back__web { position: absolute; left: 48px; bottom: 36px; color: var(--paper); font-size: 17px; letter-spacing: 0.3px; }
</style>
</head>
<body>
  <section class="card card--front" aria-label="Card front">
    <div class="brand">
      <span class="brand__dot"></span>
      <div class="brand__text">
        <span class="brand__name">ParityLumen</span>
        <span class="brand__tagline">Fairness Metrics Insight</span>
      </div>
    </div>

    <div class="holder">
      <p class="holder__line">Marcus Hale <span class="holder__title">| JOB TITLE</span></p>
      <p class="holder__address">Your Address Goes here, City, Zip Code,<br>State, Country Name</p>
    </div>

    <div class="contacts">
      <div class="contacts__row">
        <span class="contact">
          <svg viewBox="0 0 16 16"><path fill="#f39a1e" d="M3.5 1.5l2.3 2.6-1.3 1.8c.9 2 2.5 3.6 4.6 4.6l1.8-1.3 2.6 2.3-1.6 2.2C6.3 13.5 2.5 9.7 1.3 3.1z"/></svg>
          000.000.0000
        </span>
        <span class="contact">
          <svg viewBox="0 0 16 16"><rect x="2" y="3" width="12" height="10" rx="1.5" fill="#f39a1e"/><rect x="4" y="5" width="8" height="4" fill="#fff"/></svg>
          000.000.0000
        </span>
      </div>
      <div class="contacts__row">
        <span class="contact"><span class="contact__square"></span>@Parity_Lumen</span>
        <span class="contact">
          <svg viewBox="0 0 16 16"><rect x="1.5" y="3.5" width="13" height="9" rx="1" fill="#f39a1e"/><path d="M2 4l6 5 6-5" fill="none" stroke="#fff" stroke-width="1.3"/></svg>
          @paritylumen.com
        </span>
        <span class="contact">
          <svg viewBox="0 0 16 16"><circle cx="8" cy="8" r="6.5" fill="#f39a1e"/><path d="M1.5 8h13M8 1.5c-3 3.5-3 9.5 0 13M8 1.5c3 3.5 3 9.5 0 13" fill="none" stroke="#fff" stroke-width="1"/></svg>
          www.paritylumen.com
        </span>
      </div>
    </div>
  </section>

  <section class="card card--back" aria-label="Card back">
    <div class="brand">
      <span class="brand__dot"></span>
      <div class="brand__text">
        <span class="brand__name">ParityLumen</span>
        <span class="brand__tagline">Fairness Metrics Insight</span>
      </div>
    </div>
    <p class="back__web">www.paritylumen.com</p>
  </section>
</body>
</html>
```